Corvath Insurance Stationery Design Project

We need a stationery design for business cards, letterhead and envelopes.

Please refer to attached brief for further information.

Business

```html
<!DOCTYPE html>
<html lang="en">
<head>
<meta charset="utf-8">
<title>Corvath Insurance – Business Card</title>
<link rel="stylesheet" href="https://fonts.googleapis.com/css2?family=Open+Sans:wght@400;600;700&display=swap">
<style>
  :root {
    --backdrop: #b48a2a;
    --card-white: #ffffff;
    --card-grey: #cccccc;
    --band-grey: #c8c8c8;
    --accent-orange: #f47a20;
    --logo-grey: #b9b9b9;
    --text-dark: #2b2b2b;
    --text-white: #ffffff;
  }
  * { margin: 0; padding: 0; box-sizing: border-box; }
  html, body { width: 1200px; height: 686px; overflow: hidden; }
  body {
    background: var(--backdrop);
    font-family: "Open Sans", sans-serif;
    color: var(--text-dark);
    position: relative;
  }
  .card {
    position: absolute;
    width: 524px;
    height: 298px;
    box-shadow: 2px 3px 5px rgba(0,0,0,0.45);
  }
  .card--front { left: 55px; top: 157px; background: var(--card-white); }
  .card--back { left: 612px; top: 241px; background: var(--card-grey); }

  .tagline-band {
    position: absolute;
    left: 137px; top: 24px;
    width: 387px; height: 17px;
    background: var(--band-grey);
    border-radius: 9px 0 0 9px;
    color: var(--text-white);
    font-weight: 700;
    font-size: 12.5px;
    line-height: 17px;
    padding-left: 15px;
  }

  .brand {
    position: absolute;
    left: 29px; top: 108px;
    font-size: 25px;
    font-weight: 600;
    line-height: 32px;
    color: var(--logo-grey);
    letter-spacing: 0.2px;
  }

  .name-band {
    position: absolute;
    left: 303px; top: 99px;
    width: 221px; height: 18px;
    background: var(--accent-orange);
    border-radius: 9px 0 0 9px;
    color: var(--text-white);
    display: flex; align-items: center; justify-content: flex-end;
    padding-right: 26px;
  }
  .name-band__name { font-weight: 700; font-size: 13.5px; }
  .name-band__divider {
    width: 1px; height: 12px; background: var(--text-white);
    margin: 0 8px 0 10px;
  }
  .name-band__role { font-weight: 700; font-size: 11px; }

  .address {
    position: absolute;
    right: 35px; top: 140px;
    text-align: right;
    font-size: 11.2px;
    line-height: 15.4px;
    font-style: normal;
  }
  .contact {
    position: absolute;
    right: 35px; top: 210px;
    text-align: right;
    font-size: 11.2px;
    line-height: 18px;
    list-style: none;
  }
  .contact__label { color: var(--accent-orange); font-weight: 700; }

  .disclosure {
    position: absolute;
    left: 29px; top: 178px;
    width: 300px;
    font-size: 11.2px;
    line-height: 17px;
  }

  .back-brand {
    position: absolute;
    left: 26px; top: 110px;
    font-size: 26px;
    font-weight: 700;
    line-height: 32px;
    color: var(--text-white);
  }
  .website {
    position: absolute;
    left: 235px; top: 133px;
    font-size: 15px;
    line-height: 20px;
    color: var(--text-white);
    text-shadow: 0 1px 1px rgba(0,0,0,0.2);
    letter-spacing: 0.2px;
  }
</style>
</head>
<body>
  <section class="card card--front">
    <div class="tagline-band">Business and Life Insurance Brokers and Advisers</div>

    <div class="brand">Corvath Insurance</div>

    <div class="name-band">
      <span class="name-band__name">Alan Corvath</span>
      <span class="name-band__divider"></span>
      <span class="name-band__role">Director</span>
    </div>

    <address class="address">
      Level 4, 18 Harlow St<br>
      Eastwood Bay NSW 2071<br>
      PO Box 418<br>
      Eastwood Bay NSW 2070
    </address>

    <ul class="contact">
      <li><span class="contact__label">T</span> : (02) 5550 1842</li>
      <li><span class="contact__label">F</span> : (02) 5550 1843</li>
      <li><span class="contact__label">M</span> : 0400 555 219</li>
      <li><span class="contact__label">E</span> : acorvath@mvn.net.au</li>
    </ul>

    <p class="disclosure">
      Authorised Representative No. 402183<br>
      Meridale Advisory Network Pty Limited<br>
      AFSL 310772 Meridale Advisory Financial Services<br>
      Pty Ltd and its advisers are members of Tallowin<br>
      Financial Advisers and Authorised Representatives<br>
      of Brookvale Advice group Pty Ltd AFSL 291640
    </p>
  </section>

  <section class="card card--back">
    <div class="back-brand">Corvath<br>Insurance</div>
    <div class="website">www.corvathinsurance.com.au</div>
  </section>
</body>
</html>
```